Certified Legal Nurse Consultant business needs a postcard design

Need a postcard that advertises to target market of attorneys. I am a registered nurse who helps lawyers with the medical issues on their cases. I want this card to highlight the benefit of my services versus the competition. Please see attached document for more info.
Updates

Reason: Many of the 20 designs I received were from the same designer, but just altered slightly. I was expecting ~20 original/unique designs. Thanks!

Target Market(s)

attorneys (lawyers)

Industry/Entity Type

Business

Font styles to use
Serif

Colors
3176b5
0355a3

Requirements
Must have
• my photo, business name and address, phone number, web address, description of how my business is better than the competition (see PDF file sent)

```html
<!DOCTYPE html>
<html lang="en">
<head>
<meta charset="utf-8">
<title>M. Halvorsen &amp; Associates LLC — Postcard</title>
<link href="https://fonts.googleapis.com/css2?family=Cormorant+Garamond:wght@400;500;600&display=swap" rel="stylesheet">
<style>
  :root {
    --blue: #5c7fb6;
    --blue-deep: #4a6ca6;
    --mist: #e3e7ec;
    --mist-light: #eef0f3;
    --ink: #3a4a66;
    --ink-soft: #4d5d78;
    --white: #ffffff;
    --photo-dark: #2a2d33;
  }
  * { box-sizing: border-box; margin: 0; padding: 0; }
  html, body {
    width: 903px; height: 1200px; overflow: hidden;
    background: var(--white);
    font-family: "Cormorant Garamond", Georgia, serif;
  }
  .postcard {
    position: absolute; left: 0; width: 903px; height: 452px;
    background: var(--blue); overflow: hidden;
  }
  .postcard--front { top: 117px; }
  .postcard--back { top: 645px; }
  .postcard__art { position: absolute; inset: 0; width: 903px; height: 452px; }

  /* Front */
  .brand {
    position: absolute; left: 368px; top: 26px; width: 430px;
    text-align: center; color: var(--white);
    font-size: 29px; font-weight: 500; letter-spacing: 0.3px;
  }
  .brand__rule {
    position: absolute; left: 368px; top: 70px; width: 430px; height: 3px;
    background: var(--mist);
  }
  .intro-band {
    position: absolute; left: 273px; top: 100px; width: 630px; height: 56px;
    background: var(--mist);
    display: flex; align-items: center; justify-content: center;
  }
  .intro-band p {
    width: 460px; text-align: center; color: var(--ink);
    font-size: 14.5px; line-height: 1.25; font-weight: 500;
  }
  .contact {
    position: absolute; top: 372px; color: var(--ink);
    font-size: 14px; line-height: 1.45; font-weight: 500;
  }
  .contact--person { right: 192px; text-align: right; }
  .contact--office { left: 733px; }
  .contact__spacer { display: block; height: 10px; }

  /* Back */
  .panel-title {
    position: absolute; top: 33px; height: 37px;
    background: var(--mist);
    display: flex; align-items: center; justify-content: center;
    color: var(--blue-deep); font-size: 21px; font-weight: 500;
  }
  .panel-title--services { left: 0; width: 419px; }
  .panel-title--benefits { left: 478px; width: 425px; }
  .bullet-list {
    position: absolute; list-style: none;
    color: var(--mist-light); font-size: 14px; line-height: 1.2; font-weight: 500;
  }
  .bullet-list li { position: relative; padding-left: 22px; }
  .bullet-list li::before {
    content: ""; position: absolute; left: 3px; top: 4px;
    width: 10px; height: 10px; border-radius: 50%; background: var(--mist);
  }
  .bullet-list--services { left: 27px; top: 97px; width: 400px; }
  .bullet-list--benefits { left: 476px; top: 96px; width: 410px; }
  .bullet-list--benefits li { margin-bottom: 14px; }
  .bullet-list--benefits .sub { display: block; padding-left: 4px; }
  .bullet-list--benefits .sub-indent { display: block; padding-left: 14px; }
</style>
</head>
<body>

<section class="postcard postcard--front">
  <svg class="postcard__art" viewBox="0 0 903 452" aria-hidden="true">
    <defs>
      <linearGradient id="frontMist" x1="0" y1="0" x2="1" y2="0">
        <stop offset="0" stop-color="#5c7fb6"/>
        <stop offset="0.45" stop-color="#d5dce6"/>
        <stop offset="1" stop-color="#eceef1"/>
      </linearGradient>
    </defs>
    <path d="M180 452 C 420 400 660 340 903 300 L903 452 Z" fill="url(#frontMist)"/>
    <g fill="none" stroke="#ffffff" stroke-linecap="round">
      <path d="M150 420 C 420 340 660 270 903 205" stroke-width="9" opacity="0.85"/>
      <path d="M150 432 C 420 360 660 300 903 238" stroke-width="6" opacity="0.8"/>
      <path d="M150 442 C 420 378 660 322 903 262" stroke-width="8" opacity="0.85"/>
      <path d="M150 450 C 420 392 660 342 903 290" stroke-width="5" opacity="0.7"/>
    </g>
  </svg>
  <svg class="postcard__art" viewBox="0 0 903 452" role="img" aria-label="Portrait photograph of the nurse consultant in a dark blazer and white blouse">
    <defs>
      <radialGradient id="portraitTone" cx="0.45" cy="0.4" r="0.7">
        <stop offset="0" stop-color="#5a4a44"/>
        <stop offset="0.6" stop-color="#34363c"/>
        <stop offset="1" stop-color="#22242a"/>
      </radialGradient>
    </defs>
    <path d="M0 0 L210 0 C 300 120 300 330 215 452 L0 452 Z" fill="url(#portraitTone)"/>
  </svg>

  <h1 class="brand">M. Halvorsen &amp; Associates LLC</h1>
  <div class="brand__rule"></div>
  <div class="intro-band">
    <p>Certified Legal Nurse Consultant (CLNC) and Registered Nurse (RN) with over 26 years experience. Help attorneys effectively develop the medical-related issues in their cases.</p>
  </div>
  <address class="contact contact--person" style="font-style:normal">
    Mara Halvorsen<span class="contact__spacer"></span>
    (612) 555-0147<br>
    mara@halvorsen-associates.com
  </address>
  <address class="contact contact--office" style="font-style:normal;top:364px">
    M. Halvorsen &amp; Associates LLC<br>
    2190 Larkspur Lane<br>
    Cedar Bend, MN 55010<span class="contact__spacer"></span>
    www.halvorsen-associates.com
  </address>
</section>

<section class="postcard postcard--back">
  <svg class="postcard__art" viewBox="0 0 903 452" aria-hidden="true">
    <defs>
      <linearGradient id="backMist" x1="0" y1="0" x2="1" y2="0">
        <stop offset="0" stop-color="#eceef1"/>
        <stop offset="0.5" stop-color="#c9d2df"/>
        <stop offset="1" stop-color="#5c7fb6"/>
      </linearGradient>
    </defs>
    <path d="M0 330 C 300 340 620 400 903 440 L903 452 L0 452 Z" fill="url(#backMist)"/>
    <g fill="none" stroke="#ffffff" stroke-linecap="round">
      <path d="M0 285 C 300 300 620 350 903 392" stroke-width="9" opacity="0.85"/>
      <path d="M0 300 C 300 316 620 368 903 408" stroke-width="6" opacity="0.8"/>
      <path d="M0 314 C 300 332 620 386 903 424" stroke-width="8" opacity="0.85"/>
      <path d="M0 328 C 300 348 620 402 903 440" stroke-width="5" opacity="0.7"/>
    </g>
  </svg>

  <h2 class="panel-title panel-title--services">Examples of CLNC services I provide</h2>
  <h2 class="panel-title panel-title--benefits">Why our service is good for you ?</h2>

  <ul class="bullet-list bullet-list--services">
    <li>Screen cases for merit</li>
    <li>Develop medical summaries</li>
    <li>Research authoritative literature</li>
    <li>Locate testifying experts</li>
    <li>Identify adherences to and deviations from standard of care</li>
  </ul>

  <ul class="bullet-list bullet-list--benefits">
    <li>Saves time (allows attorney time to focus on legal matters)</li>
    <li>Saves money
      <span class="sub">A) cost effective for CLNC to manage medical issues versus MD</span>
      <span class="sub">or attorney completing the review</span>
      <span class="sub">B) early identification of critical issues in case can help with decision</span>
      <span class="sub-indent">making (e.g. weed out non-meritorius cases or move to settlement)</span>
      <span class="sub-indent">— this saves time too</span>
    </li>
    <li>Bring healthcare expertise to the development of case</li>
  </ul>
</section>

</body>
</html>
```